Copper Ridge Stewardship Summit needs a marketing flyer

We need a full page graphic for our upcoming Forum that can also be converted into a website "header" for social media, etc.: "Copper Ridge Stewardship Summit - Making Impact Through the Built Environment"

INTRODUCTION:
During the first week of August 2022, Q-VarDT is presenting the Copper Ridge Stewardship Summit - Making Impact Through the Built Environment.

One of the most exciting aspects of this conference will be the bringing together of multiple organizations including for-profits and nonprofits, K-12’s and higher education, cities and counties and other governmental agencies, as well as architects, engineers, and contractors to collaboratively present and discuss issues and ideas related to sustainability, with a Texas focus.

This event will be a catalyst for public and private project owners to holistically gather information and momentum as we bring the resources and vision needed to achieve the goal of zero carbon emissions from the built environment by 2040, and address water, green space and the natural environment, transportation, equity, and funding, among other topics.

```html
<!DOCTYPE html>
<html lang="en">
<head>
<meta charset="utf-8">
<title>Copper Ridge Stewardship Summit – Flyer</title>
<link href="https://fonts.googleapis.com/css2?family=Lexend:wght@400;500;600;700;800&display=swap" rel="stylesheet">
<style>
:root{
  --blue:#3451a3;
  --blue-deep:#2c4699;
  --green:#82b541;
  --green-dark:#6fa332;
  --ink:#2f2f33;
  --grey-block:#4b4b4f;
  --rule:#d9dbe2;
  --paper:#ffffff;
  --page:#f2f2f0;
}
*{margin:0;padding:0;box-sizing:border-box}
html,body{width:1200px;height:3000px;overflow:hidden}
body{background:var(--page);font-family:"Lexend",Arial,sans-serif;color:var(--ink);position:relative}

.flyer{position:absolute;width:844px;height:1127px;background:var(--paper);overflow:hidden;transform-origin:0 0;box-shadow:0 6px 18px rgba(0,0,0,.18)}
.flyer--upper{left:315px;top:172px;transform:scale(.917)}
.flyer--lower{left:178px;top:1682px}

.hero-photo{position:absolute;left:0;top:0;width:844px;height:640px;
  background:
    radial-gradient(ellipse 160px 200px at 430px 330px,rgba(255,255,235,.95),rgba(255,248,170,.55) 45%,rgba(0,0,0,0) 75%),
    radial-gradient(ellipse 380px 300px at 560px 180px,rgba(250,220,80,.8),rgba(0,0,0,0) 70%),
    linear-gradient(90deg,#2f6b1c 0%,#5d9a2a 25%,#a6c43a 50%,#6f9e26 75%,#3d7a20 100%)}
.shapes{position:absolute;left:0;top:0}

.title{position:absolute;left:60px;width:724px;text-align:center;color:#fff;font-weight:700;line-height:1;letter-spacing:-.5px}
.title__line1{top:414px;font-size:56px}
.title__line2{top:478px;font-size:58px}
.title__line3{top:540px;font-size:74px;font-weight:800}

.tagline{position:absolute;left:0;width:844px;top:676px;text-align:center;color:var(--green);font-weight:700;font-size:31px;letter-spacing:-.3px}

.date-badge{position:absolute;left:63px;top:733px;height:55px;display:flex;border-radius:7px;overflow:hidden}
.date-badge__lead{background:var(--blue);color:#fff;display:flex;align-items:center;padding:0 10px 0 14px;gap:10px}
.date-badge__small{font-size:16px;line-height:1.05;font-weight:500}
.date-badge__month{font-size:42px;font-weight:600;letter-spacing:-.5px}
.date-badge__year{background:var(--grey-block);color:#fff;font-size:44px;font-weight:600;display:flex;align-items:center;padding:0 10px;margin-left:3px}

.intro{position:absolute;left:63px;top:806px;width:430px;font-size:15.5px;font-weight:500;line-height:1.25;color:var(--ink)}
.highlight{position:absolute;left:63px;top:853px;width:440px;font-size:15.5px;font-weight:700;line-height:1.27;color:var(--blue-deep)}

.audience{position:absolute;top:928px;list-style:none;font-size:13.5px;line-height:1.2}
.audience--left{left:62px;width:210px}
.audience--right{left:270px;width:225px;top:920px}
.audience li{position:relative;padding-left:20px;margin-bottom:17px}
.audience--right li{margin-bottom:15px}
.tick{position:absolute;left:0;top:2px;width:11px;height:11px}

.vision{position:absolute;left:514px;top:731px;width:269px;height:286px;border:1.5px solid var(--blue);border-radius:10px;overflow:hidden;background:#fff}
.vision__band{position:absolute;left:0;top:0}
.vision__label{position:absolute;left:-60px;top:170px;width:180px;text-align:center;transform:rotate(-90deg);color:#fff;font-size:30px;font-weight:600;letter-spacing:1px}
.vision__icon{position:absolute;left:12px;top:52px}
.vision__goal{position:absolute;left:74px;top:16px;width:185px;font-size:13px;line-height:1.18;font-weight:500}
.vision__goal em{font-style:normal;color:var(--blue)}
.vision__list{position:absolute;left:68px;top:98px;width:185px;list-style:none;font-size:13px}
.vision__list li{position:relative;padding:5px 0 5px 32px;border-bottom:1px solid var(--rule)}
.vision__list li:last-child{border-bottom:none}
.vision__list .tick{left:4px;top:8px}

.footer-rule{position:absolute;left:53px;right:53px;top:1042px;height:1px;background:var(--rule)}
.footer{position:absolute;left:60px;top:1060px;width:740px;height:44px;display:flex;align-items:center;gap:18px}
.brand{display:flex;align-items:center;gap:9px;margin-right:20px}
.brand__dot{width:38px;height:38px;border-radius:50%;background:var(--blue)}
.brand__name{font-size:25px;font-weight:500;color:var(--blue)}
.contact{display:flex;align-items:center;gap:6px;color:var(--ink);font-weight:500}
.contact--phone{font-size:23px}
.contact--mail,.contact--web{font-size:16px}
</style>
</head>
<body>

<article class="flyer flyer--upper" aria-label="Summit flyer">
  <div class="hero-photo" role="img" aria-label="Glowing light bulb held up against a sunlit green forest with sustainability icons"></div>
  <svg class="shapes" width="844" height="1127" viewBox="0 0 844 1127" aria-hidden="true">
    <polygon points="0,420 72,525 0,660" fill="var(--green)"/>
    <polygon points="844,420 772,525 844,660" fill="var(--green)"/>
    <path d="M0,660 L72,525 Q422,780 772,525 L844,660 L844,1127 L0,1127 Z" fill="#fff"/>
    <ellipse cx="422" cy="505" rx="378" ry="162" fill="#fff"/>
    <ellipse cx="422" cy="505" rx="366" ry="152" fill="var(--blue)"/>
  </svg>
  <div class="title title__line1">COPPER RIDGE</div>
  <div class="title title__line2">STEWARDSHIP</div>
  <div class="title title__line3">SUMMIT</div>
  <div class="tagline">Making Impact Through the Built Environment</div>
  <div class="date-badge">
    <div class="date-badge__lead"><span class="date-badge__small">During the<br>first week of</span><span class="date-badge__month">AUGUST</span></div>
    <div class="date-badge__year">2022</div>
  </div>
  <p class="intro">Q-VarDT is presenting the Copper Ridge Stewardship Summit Making Impact Through the Built Environment.</p>
  <p class="highlight">One of the most exciting aspects of this conference will be the bringing together of multiple organizations including for-</p>
  <ul class="audience audience--left">
    <li><svg class="tick" viewBox="0 0 12 12"><circle cx="6" cy="6" r="5" fill="none" stroke="#82b541" stroke-width="1.3"/><path d="M3.5 6.2l1.8 1.7 3.3-3.4" fill="none" stroke="#82b541" stroke-width="1.3"/></svg>Profits and nonprofits,</li>
    <li><svg class="tick" viewBox="0 0 12 12"><circle cx="6" cy="6" r="5" fill="none" stroke="#82b541" stroke-width="1.3"/><path d="M3.5 6.2l1.8 1.7 3.3-3.4" fill="none" stroke="#82b541" stroke-width="1.3"/></svg>K-12’s and higher education,</li>
    <li><svg class="tick" viewBox="0 0 12 12"><circle cx="6" cy="6" r="5" fill="none" stroke="#82b541" stroke-width="1.3"/><path d="M3.5 6.2l1.8 1.7 3.3-3.4" fill="none" stroke="#82b541" stroke-width="1.3"/></svg>Cities and counties and other governmental agencies,</li>
  </ul>
  <ul class="audience audience--right">
    <li><svg class="tick" viewBox="0 0 12 12"><circle cx="6" cy="6" r="5" fill="none" stroke="#82b541" stroke-width="1.3"/><path d="M3.5 6.2l1.8 1.7 3.3-3.4" fill="none" stroke="#82b541" stroke-width="1.3"/></svg>Architects &amp; engineers,</li>
    <li><svg class="tick" viewBox="0 0 12 12"><circle cx="6" cy="6" r="5" fill="none" stroke="#82b541" stroke-width="1.3"/><path d="M3.5 6.2l1.8 1.7 3.3-3.4" fill="none" stroke="#82b541" stroke-width="1.3"/></svg>Contractors to collaboratively present and discuss issues and ideas related to sustainability, with a Texas focus.</li>
  </ul>
  <section class="vision">
    <svg class="vision__band" width="66" height="286" viewBox="0 0 66 286" aria-hidden="true"><path d="M0,0 L30,0 Q66,10 64,60 L64,226 Q66,276 30,286 L0,286 Z" fill="var(--green)"/></svg>
    <svg class="vision__icon" width="40" height="34" viewBox="0 0 40 34" aria-hidden="true"><path d="M3 20 Q20 4 37 20 Q20 34 3 20Z" fill="none" stroke="#fff" stroke-width="2.5"/><circle cx="20" cy="20" r="6" fill="none" stroke="#fff" stroke-width="2.5"/><circle cx="20" cy="20" r="2.3" fill="#fff"/><path d="M20 2v5M9 5l3 4M31 5l-3 4" stroke="#fff" stroke-width="2.5"/></svg>
    <div class="vision__label">VISION</div>
    <p class="vision__goal">Achieve the goal of zero carbon emissions from the <em>built environment by 2040.</em></p>
    <ul class="vision__list">
      <li><svg class="tick" viewBox="0 0 12 12"><circle cx="6" cy="6" r="5" fill="none" stroke="#82b541" stroke-width="1.3"/><path d="M3.5 6.2l1.8 1.7 3.3-3.4" fill="none" stroke="#82b541" stroke-width="1.3"/></svg>Address water</li>
      <li><svg class="tick" viewBox="0 0 12 12"><circle cx="6" cy="6" r="5" fill="none" stroke="#82b541" stroke-width="1.3"/><path d="M3.5 6.2l1.8 1.7 3.3-3.4" fill="none" stroke="#82b541" stroke-width="1.3"/></svg>Green space and the</li>
      <li><svg class="tick" viewBox="0 0 12 12"><circle cx="6" cy="6" r="5" fill="none" stroke="#82b541" stroke-width="1.3"/><path d="M3.5 6.2l1.8 1.7 3.3-3.4" fill="none" stroke="#82b541" stroke-width="1.3"/></svg>Natural environment,</li>
      <li><svg class="tick" viewBox="0 0 12 12"><circle cx="6" cy="6" r="5" fill="none" stroke="#82b541" stroke-width="1.3"/><path d="M3.5 6.2l1.8 1.7 3.3-3.4" fill="none" stroke="#82b541" stroke-width="1.3"/></svg>Transportation,</li>
      <li><svg class="tick" viewBox="0 0 12 12"><circle cx="6" cy="6" r="5" fill="none" stroke="#82b541" stroke-width="1.3"/><path d="M3.5 6.2l1.8 1.7 3.3-3.4" fill="none" stroke="#82b541" stroke-width="1.3"/></svg>Equity,</li>
      <li><svg class="tick" viewBox="0 0 12 12"><circle cx="6" cy="6" r="5" fill="none" stroke="#82b541" stroke-width="1.3"/><path d="M3.5 6.2l1.8 1.7 3.3-3.4" fill="none" stroke="#82b541" stroke-width="1.3"/></svg>Funding,</li>
      <li><svg class="tick" viewBox="0 0 12 12"><circle cx="6" cy="6" r="5" fill="none" stroke="#82b541" stroke-width="1.3"/><path d="M3.5 6.2l1.8 1.7 3.3-3.4" fill="none" stroke="#82b541" stroke-width="1.3"/></svg>Among other topics.</li>
    </ul>
  </section>
  <div class="footer-rule"></div>
  <footer class="footer">
    <div class="brand"><span class="brand__dot"></span><span class="brand__name">Q-VarDT</span></div>
    <span class="contact contact--phone"><svg width="18" height="18" viewBox="0 0 24 24" aria-hidden="true"><path d="M6.6 10.8a15 15 0 006.6 6.6l2.2-2.2a1 1 0 011-.25 11.4 11.4 0 003.6.6 1 1 0 011 1V20a1 1 0 01-1 1A17 17 0 013 4a1 1 0 011-1h3.5a1 1 0 011 1c0 1.25.2 2.45.6 3.6a1 1 0 01-.25 1z" fill="var(--blue)"/></svg>1234567890</span>
    <span class="contact contact--mail"><svg width="18" height="14" viewBox="0 0 18 14" aria-hidden="true"><rect x="1" y="1" width="16" height="12" rx="1.5" fill="none" stroke="var(--blue)" stroke-width="2"/><path d="M1.5 2l7.5 6 7.5-6" fill="none" stroke="var(--blue)" stroke-width="2"/></svg>info@Q-VarDT.com</span>
    <span class="contact contact--web"><svg width="17" height="17" viewBox="0 0 20 20" aria-hidden="true"><circle cx="10" cy="10" r="8.5" fill="none" stroke="var(--blue)" stroke-width="1.8"/><ellipse cx="10" cy="10" rx="3.8" ry="8.5" fill="none" stroke="var(--blue)" stroke-width="1.5"/><path d="M1.5 10h17M3 5.5h14M3 14.5h14" stroke="var(--blue)" stroke-width="1.3"/></svg>www.Q-VarDT.com</span>
  </footer>
</article>

<article class="flyer flyer--lower" aria-label="Summit flyer">
  <div class="hero-photo" role="img" aria-label="Glowing light bulb held up against a sunlit green forest with sustainability icons"></div>
  <svg class="shapes" width="844" height="1127" viewBox="0 0 844 1127" aria-hidden="true">
    <polygon points="0,420 72,525 0,660" fill="var(--green)"/>
    <polygon points="844,420 772,525 844,660" fill="var(--green)"/>
    <path d="M0,660 L72,525 Q422,780 772,525 L844,660 L844,1127 L0,1127 Z" fill="#fff"/>
    <ellipse cx="422" cy="505" rx="378" ry="162" fill="#fff"/>
    <ellipse cx="422" cy="505" rx="366" ry="152" fill="var(--blue)"/>
  </svg>
  <div class="title title__line1">COPPER RIDGE</div>
  <div class="title title__line2">STEWARDSHIP</div>
  <div class="title title__line3">SUMMIT</div>
  <div class="tagline">Making Impact Through the Built Environment</div>
  <div class="date-badge">
    <div class="date-badge__lead"><span class="date-badge__small">During the<br>first week of</span><span class="date-badge__month">AUGUST</span></div>
    <div class="date-badge__year">2022</div>
  </div>
  <p class="intro">Q-VarDT is presenting the Copper Ridge Stewardship Summit Making Impact Through the Built Environment.</p>
  <p class="highlight">One of the most exciting aspects of this conference will be the bringing together of multiple organizations including for-</p>
  <ul class="audience audience--left">
    <li><svg class="tick" viewBox="0 0 12 12"><circle cx="6" cy="6" r="5" fill="none" stroke="#82b541" stroke-width="1.3"/><path d="M3.5 6.2l1.8 1.7 3.3-3.4" fill="none" stroke="#82b541" stroke-width="1.3"/></svg>Profits and nonprofits,</li>
    <li><svg class="tick" viewBox="0 0 12 12"><circle cx="6" cy="6" r="5" fill="none" stroke="#82b541" stroke-width="1.3"/><path d="M3.5 6.2l1.8 1.7 3.3-3.4" fill="none" stroke="#82b541" stroke-width="1.3"/></svg>K-12’s and higher education,</li>
    <li><svg class="tick" viewBox="0 0 12 12"><circle cx="6" cy="6" r="5" fill="none" stroke="#82b541" stroke-width="1.3"/><path d="M3.5 6.2l1.8 1.7 3.3-3.4" fill="none" stroke="#82b541" stroke-width="1.3"/></svg>Cities and counties and other governmental agencies,</li>
  </ul>
  <ul class="audience audience--right">
    <li><svg class="tick" viewBox="0 0 12 12"><circle cx="6" cy="6" r="5" fill="none" stroke="#82b541" stroke-width="1.3"/><path d="M3.5 6.2l1.8 1.7 3.3-3.4" fill="none" stroke="#82b541" stroke-width="1.3"/></svg>Architects &amp; engineers,</li>
    <li><svg class="tick" viewBox="0 0 12 12"><circle cx="6" cy="6" r="5" fill="none" stroke="#82b541" stroke-width="1.3"/><path d="M3.5 6.2l1.8 1.7 3.3-3.4" fill="none" stroke="#82b541" stroke-width="1.3"/></svg>Contractors to collaboratively present and discuss issues and ideas related to sustainability, with a Texas focus.</li>
  </ul>
  <section class="vision">
    <svg class="vision__band" width="66" height="286" viewBox="0 0 66 286" aria-hidden="true"><path d="M0,0 L30,0 Q66,10 64,60 L64,226 Q66,276 30,286 L0,286 Z" fill="var(--green)"/></svg>
    <svg class="vision__icon" width="40" height="34" viewBox="0 0 40 34" aria-hidden="true"><path d="M3 20 Q20 4 37 20 Q20 34 3 20Z" fill="none" stroke="#fff" stroke-width="2.5"/><circle cx="20" cy="20" r="6" fill="none" stroke="#fff" stroke-width="2.5"/><circle cx="20" cy="20" r="2.3" fill="#fff"/><path d="M20 2v5M9 5l3 4M31 5l-3 4" stroke="#fff" stroke-width="2.5"/></svg>
    <div class="vision__label">VISION</div>
    <p class="vision__goal">Achieve the goal of zero carbon emissions from the <em>built environment by 2040.</em></p>
    <ul class="vision__list">
      <li><svg class="tick" viewBox="0 0 12 12"><circle cx="6" cy="6" r="5" fill="none" stroke="#82b541" stroke-width="1.3"/><path d="M3.5 6.2l1.8 1.7 3.3-3.4" fill="none" stroke="#82b541" stroke-width="1.3"/></svg>Address water</li>
      <li><svg class="tick" viewBox="0 0 12 12"><circle cx="6" cy="6" r="5" fill="none" stroke="#82b541" stroke-width="1.3"/><path d="M3.5 6.2l1.8 1.7 3.3-3.4" fill="none" stroke="#82b541" stroke-width="1.3"/></svg>Green space and the</li>
      <li><svg class="tick" viewBox="0 0 12 12"><circle cx="6" cy="6" r="5" fill="none" stroke="#82b541" stroke-width="1.3"/><path d="M3.5 6.2l1.8 1.7 3.3-3.4" fill="none" stroke="#82b541" stroke-width="1.3"/></svg>Natural environment,</li>
      <li><svg class="tick" viewBox="0 0 12 12"><circle cx="6" cy="6" r="5" fill="none" stroke="#82b541" stroke-width="1.3"/><path d="M3.5 6.2l1.8 1.7 3.3-3.4" fill="none" stroke="#82b541" stroke-width="1.3"/></svg>Transportation,</li>
      <li><svg class="tick" viewBox="0 0 12 12"><circle cx="6" cy="6" r="5" fill="none" stroke="#82b541" stroke-width="1.3"/><path d="M3.5 6.2l1.8 1.7 3.3-3.4" fill="none" stroke="#82b541" stroke-width="1.3"/></svg>Equity,</li>
      <li><svg class="tick" viewBox="0 0 12 12"><circle cx="6" cy="6" r="5" fill="none" stroke="#82b541" stroke-width="1.3"/><path d="M3.5 6.2l1.8 1.7 3.3-3.4" fill="none" stroke="#82b541" stroke-width="1.3"/></svg>Funding,</li>
      <li><svg class="tick" viewBox="0 0 12 12"><circle cx="6" cy="6" r="5" fill="none" stroke="#82b541" stroke-width="1.3"/><path d="M3.5 6.2l1.8 1.7 3.3-3.4" fill="none" stroke="#82b541" stroke-width="1.3"/></svg>Among other topics.</li>
    </ul>
  </section>
  <div class="footer-rule"></div>
  <footer class="footer">
    <div class="brand"><span class="brand__dot"></span><span class="brand__name">Q-VarDT</span></div>
    <span class="contact contact--phone"><svg width="18" height="18" viewBox="0 0 24 24" aria-hidden="true"><path d="M6.6 10.8a15 15 0 006.6 6.6l2.2-2.2a1 1 0 011-.25 11.4 11.4 0 003.6.6 1 1 0 011 1V20a1 1 0 01-1 1A17 17 0 013 4a1 1 0 011-1h3.5a1 1 0 011 1c0 1.25.2 2.45.6 3.6a1 1 0 01-.25 1z" fill="var(--blue)"/></svg>1234567890</span>
    <span class="contact contact--mail"><svg width="18" height="14" viewBox="0 0 18 14" aria-hidden="true"><rect x="1" y="1" width="16" height="12" rx="1.5" fill="none" stroke="var(--blue)" stroke-width="2"/><path d="M1.5 2l7.5 6 7.5-6" fill="none" stroke="var(--blue)" stroke-width="2"/></svg>info@Q-VarDT.com</span>
    <span class="contact contact--web"><svg width="17" height="17" viewBox="0 0 20 20" aria-hidden="true"><circle cx="10" cy="10" r="8.5" fill="none" stroke="var(--blue)" stroke-width="1.8"/><ellipse cx="10" cy="10" rx="3.8" ry="8.5" fill="none" stroke="var(--blue)" stroke-width="1.5"/><path d="M1.5 10h17M3 5.5h14M3 14.5h14" stroke="var(--blue)" stroke-width="1.3"/></svg>www.Q-VarDT.com</span>
  </footer>
</article>

</body>
</html>
```